New Business Card Design Project

We require a business card design for Zelvaquin, a newly established Indian company.
Our focus is on the development, manufacturing, and export of a diverse array of pharmaceutical products on a global scale. The card should convey a professional appearance, as our primary markets are in Africa, China, and Southeast Asian nations.
We envision a two-sided business card, with the reverse side dedicated to a logo set against a solid color or an elegantly designed pattern. The corners should be rounded. We would appreciate seeing both horizontal and vertical design options. We trust the designer to utilize their expertise in creating this design.

The content for the business card is included in the attached Word file.

Target Market(s)

Our primary markets are in Africa, China, and Southeast Asian, Latin America, Maldives, Sri Lanka

Industry/Entity Type

Pharmaceutical Manufacturing and Export

Contact Information for Business Card

Colors

Designer to choose colors to be used in the design.

Requirements
Must have
• The reverse side of the business card features solely the logo along with the tagline, "Remedies of Life."
Should not have
• The logo should not exceed two instances, encompassing both the front and back sides of the card.

```html
<!DOCTYPE html>
<html lang="en">
<head>
<meta charset="utf-8">
<title>Zelvaquin Business Card</title>
<link href="https://fonts.googleapis.com/css2?family=Poppins:wght@400;600;700&display=swap" rel="stylesheet">
<style>
  :root {
    --stage: #151515;
    --card-white: #ffffff;
    --brand-blue: #1e96d8;
    --brand-blue-light: #2aa5e4;
    --brand-blue-deep: #1a87c6;
    --brand-red: #ec4c3a;
    --ink: #2b2b2b;
  }
  * { margin: 0; padding: 0; box-sizing: border-box; }
  html, body {
    width: 1200px; height: 1059px; overflow: hidden;
    background: var(--stage);
    font-family: "Poppins", sans-serif;
  }
  .canvas { position: relative; width: 1200px; height: 1059px; }

  .card {
    position: absolute; top: 182px;
    border-radius: 22px; overflow: hidden;
  }
  .card-front { left: 177px; width: 391px; height: 687px; background: var(--card-white); }
  .card-back  { left: 646px; width: 395px; height: 694px; }

  .centered { position: absolute; left: 0; width: 100%; text-align: center; white-space: nowrap; }

  .front-wordmark {
    top: 194px; font-size: 56px; font-weight: 600;
    color: var(--brand-blue); letter-spacing: -0.5px; line-height: 1.1;
  }
  .holder-name {
    top: 318px; font-size: 26px; font-weight: 700; line-height: 1.2;
    color: var(--brand-blue);
  }
  .holder-name .surname { color: var(--brand-red); }
  .holder-role {
    top: 350px; font-size: 16px; line-height: 17px; color: var(--ink);
  }

  .contact-divider {
    position: absolute; top: 414px; left: 41px; width: 310px; height: 22px;
  }
  .contact-divider .rule {
    position: absolute; top: 10px; height: 1.5px; width: 102px; background: var(--brand-red);
  }
  .contact-divider .rule.left { left: 0; }
  .contact-divider .rule.right { right: 0; }
  .icon-row {
    position: absolute; left: 50%; top: 0; transform: translateX(-50%);
    display: flex; gap: 10px;
  }
  .icon-tile {
    width: 22px; height: 22px; border-radius: 3px; background: var(--brand-blue);
    display: flex; align-items: center; justify-content: center;
  }

  .contact-list {
    top: 449px; font-size: 17.5px; line-height: 28px; color: var(--ink);
  }
  .address-rule {
    position: absolute; top: 545px; left: 41px; width: 310px; height: 1.5px;
    background: var(--brand-red);
  }
  .address {
    top: 557px; font-size: 16.8px; line-height: 23.5px; color: var(--ink);
  }

  .back-pattern {
    position: absolute; inset: 0;
    background: linear-gradient(180deg, var(--brand-blue-light) 0%, var(--brand-blue) 55%, var(--brand-blue-deep) 100%);
  }
  .back-wordmark {
    top: 398px; font-size: 62px; font-weight: 600; line-height: 1;
    color: #ffffff; letter-spacing: -0.5px;
  }
</style>
</head>
<body>
<div class="canvas">

  <section class="card card-front">
    <div class="centered front-wordmark">Zelvaquin</div>

    <div class="centered holder-name">Rohan K. <span class="surname">Tavare</span></div>
    <div class="centered holder-role">CEO<br>Zelvaquin</div>

    <div class="contact-divider">
      <span class="rule left"></span>
      <div class="icon-row">
        <span class="icon-tile" aria-label="Phone">
          <svg width="14" height="12" viewBox="0 0 14 12"><path d="M1 4c0-2 2-3 6-3s6 1 6 3v1h-3V3.5H4V5H1z" fill="#fff"/><rect x="3" y="6" width="8" height="5" rx="1" fill="#fff"/></svg>
        </span>
        <span class="icon-tile" aria-label="Email">
          <svg width="14" height="11" viewBox="0 0 14 11"><rect x="0.5" y="0.5" width="13" height="10" fill="#fff"/><path d="M0.5 0.5L7 6l6.5-5.5" stroke="#1e96d8" stroke-width="1.2" fill="none"/></svg>
        </span>
        <span class="icon-tile" aria-label="Website">
          <svg width="14" height="14" viewBox="0 0 14 14"><circle cx="7" cy="7" r="6" fill="#fff"/><path d="M4 4c1 1 2 0 3 1s-1 2 0 3 2 0 2 2M9 2.5c-1 1 0 2 1.5 2" stroke="#1e96d8" stroke-width="1.3" fill="none"/></svg>
        </span>
      </div>
      <span class="rule right"></span>
    </div>

    <div class="centered contact-list">
      +919800012345<br>
      rtavare@zelvaquin.com<br>
      www.zelvaquin.com
    </div>

    <div class="address-rule"></div>

    <div class="centered address">
      Plot No.14, Sunmeet Colony<br>
      Kesar Road, Ambivali<br>
      Pin Code: 440019, Maharashtra, India
    </div>
  </section>

  <section class="card card-back">
    <div class="back-pattern" role="img" aria-label="Repeating brand pattern on blue background"></div>
    <div class="centered back-wordmark">Zelvaquin</div>
  </section>

</div>
</body>
</html>
```